Executive search firm in fashion, luxury and retail industry needs logo and card design.

We are a start-up recruiting firm that specializes in the retail and fashion industry, based in New York. We are looking for something that will appeal to CEO level clients and candidates, but that has a little design edge...not overly corporate but still CEO-appropriate. We have clean, sophisticated taste and want a contemporary feel. Happy to have a two sided card. Not afraid of a little color but it should be high-design, not gimmicky and tasteful.

Quillmart Market(s)

CEO's, HR Leaders, in retail, fashion (i.e. Halvorsen, Quillmart, Otto Brevik)

Industry/Entity Type

Professional Service

Contact Information for Business Card

Calloway Ridge Search Partners
Address to be determined
New York, NY 10036

Marta Velard
Managing Director
(555)038-4172
mvelard@callowayridgesearch.example

Font styles to use
Serif
Sans Serif

Requirements
Must have
• clean lines, crisp graphics, some color. Prefer a graphic treatment over a "logo" per se. No pictures, etc.
Nice to have
• double sided design.
Should not have
• Gimmicks, smaltz, goop. Think Gallery of Current Works, not the Dunmore Holdings. No earth tones, as in beige and brown, no pastels. Strong colors are fine in moderation. Grays are good. Jewel tones are good. No red.

```html
<!DOCTYPE html>
<html lang="en">
<head>
<meta charset="utf-8">
<title>Calloway Ridge Search Partners – Business Card</title>
<link rel="stylesheet" href="https://fonts.googleapis.com/css2?family=Cinzel:wght@400;600&family=Open+Sans:wght@400;600&display=swap">
<style>
  :root {
    --backdrop: #1f1d1c;
    --card: #5b5b5b;
    --card-edge: #4d4d4d;
    --ink: #1d1d1d;
    --ink-soft: #2a2a2a;
    --accent: #f39a1e;
  }
  * { box-sizing: border-box; margin: 0; padding: 0; }
  html, body {
    width: 1200px; height: 716px; overflow: hidden;
    background: var(--backdrop);
  }
  .stage {
    position: relative; width: 1200px; height: 716px;
    display: flex; align-items: center; justify-content: center; gap: 60px;
  }
  .card {
    position: relative; width: 520px; height: 298px;
    background: var(--card);
    border: 1px solid var(--card-edge);
    box-shadow: 0 10px 30px rgba(0,0,0,.45);
    overflow: hidden;
  }

  /* Wordmark shared by both sides */
  .wordmark {
    display: flex; flex-direction: column; align-items: center;
    font-family: "Cinzel", serif; font-weight: 600; color: var(--ink);
  }
  .wordmark-mark { background: var(--ink); }
  .wordmark-main { line-height: 1.1; letter-spacing: .5px; white-space: nowrap; }
  .wordmark-sub {
    display: flex; align-items: center; width: 100%;
    line-height: 1.2; letter-spacing: 1px; white-space: nowrap;
  }
  .wordmark-sub::before, .wordmark-sub::after {
    content: ""; flex: 1; height: 1px; background: var(--ink);
  }
  .wordmark-sub::before { margin-right: 8px; transform: translateY(-6px); }
  .wordmark-sub::after { margin-left: 8px; transform: translateY(6px); }

  /* Front side */
  .card--front { display: flex; align-items: center; justify-content: center; }
  .card--front .wordmark { width: 340px; gap: 8px; }
  .card--front .wordmark-mark { width: 46px; height: 46px; margin-bottom: 4px; }
  .card--front .wordmark-main { font-size: 32px; }
  .card--front .wordmark-sub { font-size: 14px; }

  /* Back side */
  .card--back .wordmark {
    position: absolute; left: 34px; top: 82px; width: 210px; gap: 6px;
  }
  .card--back .wordmark-mark { width: 32px; height: 32px; background: var(--accent); margin-bottom: 4px; }
  .card--back .wordmark-main { font-size: 20px; }
  .card--back .wordmark-sub { font-size: 10px; }

  .divider {
    position: absolute; left: 266px; top: 68px;
    width: 2px; height: 112px; background: var(--accent);
  }
  .contact {
    position: absolute; left: 282px; top: 72px; width: 226px;
  }
  .contact-name {
    font-family: "Cinzel", serif; font-weight: 600;
    color: var(--accent); font-size: 19px; letter-spacing: .5px;
  }
  .contact-title {
    font-family: "Open Sans", sans-serif; font-weight: 600;
    color: var(--ink-soft); font-size: 10px; text-transform: uppercase;
    letter-spacing: .3px; margin: 2px 0 12px;
  }
  .contact-list { list-style: none; }
  .contact-item {
    display: flex; align-items: center; gap: 5px;
    font-family: "Open Sans", sans-serif; color: var(--ink);
    font-size: 10px; line-height: 16px; white-space: nowrap;
  }
  .icon {
    width: 11px; height: 11px; flex: none;
    background: var(--accent); border-radius: 2px;
    display: flex; align-items: center; justify-content: center;
  }
  .icon svg { width: 8px; height: 8px; }
  .address {
    position: absolute; left: 34px; right: 20px; bottom: 24px;
    font-family: "Open Sans", sans-serif; color: var(--ink-soft);
    font-size: 11px; letter-spacing: .4px; text-transform: uppercase;
  }
</style>
</head>
<body>
<main class="stage">
  <section class="card card--front">
    <div class="wordmark">
      <span class="wordmark-mark"></span>
      <h1 class="wordmark-main">Calloway Ridge</h1>
      <span class="wordmark-sub">Search Partners</span>
    </div>
  </section>

  <section class="card card--back">
    <div class="wordmark">
      <span class="wordmark-mark"></span>
      <p class="wordmark-main">Calloway Ridge</p>
      <span class="wordmark-sub">Search Partners</span>
    </div>
    <span class="divider"></span>
    <div class="contact">
      <h2 class="contact-name">Marta Velard</h2>
      <p class="contact-title">Managing Director</p>
      <ul class="contact-list">
        <li class="contact-item">
          <span class="icon"><svg viewBox="0 0 10 10"><path d="M2 1 L4 1 L4.6 3 L3.5 3.8 C4 5 5 6 6.2 6.5 L7 5.4 L9 6 L9 8 C9 8.6 8.5 9 8 9 C4.5 9 1 5.5 1 2 C1 1.5 1.4 1 2 1 Z" fill="#2a2a2a"/></svg></span>
          (555)038-4172
        </li>
        <li class="contact-item">
          <span class="icon"><svg viewBox="0 0 10 10"><rect x="1" y="2.2" width="8" height="5.6" fill="none" stroke="#2a2a2a" stroke-width="1.1"/><path d="M1 2.4 L5 5.6 L9 2.4" fill="none" stroke="#2a2a2a" stroke-width="1.1"/></svg></span>
          mvelard@callowayridgesearch.example
        </li>
        <li class="contact-item">
          <span class="icon"><svg viewBox="0 0 10 10"><circle cx="5" cy="5" r="3.8" fill="none" stroke="#2a2a2a" stroke-width="1"/><ellipse cx="5" cy="5" rx="1.6" ry="3.8" fill="none" stroke="#2a2a2a" stroke-width=".9"/><path d="M1.2 5 H8.8" stroke="#2a2a2a" stroke-width=".9"/></svg></span>
          www.callowayridgesearch.example
        </li>
      </ul>
    </div>
    <p class="address">The Annex, 18 Harbor Lane, Westbrook, NY 10036</p>
  </section>
</main>
</body>
</html>
```